R. K. Belvard & Associates, Inc

Gregor Belvard
Accountant
4219 NW 168th ST
Cedarbrook, Florida 33081
(305) 555-0187
greg.belvard@quillmarsh.com
Accounting - Tax Preparation Services - Bookkeeping
Side - one business logo on the left and business information on right
On Backside: The logo in the middle and under the logo my company name.

Rounded Corner of the cards
In reference to the logo and cards I need to adjust the circle around the RK and color.

```html
<!DOCTYPE html>
<html lang="en">
<head>
<meta charset="utf-8">
<title>R. K. Belvard &amp; Associates, Inc — Business Cards</title>
<link rel="stylesheet" href="https://fonts.googleapis.com/css2?family=Red+Hat+Display:wght@400;500;600&display=swap">
<style>
  :root {
    --page-bg: #e3e3e3;
    --brand-blue: #0a6db4;
    --card-white: #f4f4f4;
    --ink: #222222;
    --rule: #555555;
    --white: #ffffff;
  }
  * { margin: 0; padding: 0; box-sizing: border-box; }
  html, body { width: 1200px; height: 960px; overflow: hidden; }
  body {
    background: var(--page-bg);
    font-family: "Red Hat Display", Arial, sans-serif;
    position: relative;
  }
  .card {
    position: absolute;
    left: 303px;
    width: 598px;
    height: 341px;
    border-radius: 22px;
    overflow: hidden;
  }
  .card--front { top: 120px; background: var(--brand-blue); }
  .card--back { top: 515px; background: var(--card-white); }

  .front-mark {
    position: absolute;
    left: 0; right: 0; top: 90px;
    text-align: center;
    color: var(--white);
    font-weight: 500;
    font-size: 96px;
    line-height: 1;
    letter-spacing: 2px;
  }
  .front-company {
    position: absolute;
    left: 0; right: 0; top: 260px;
    text-align: center;
    color: var(--white);
    font-weight: 500;
    font-size: 21px;
  }

  .back-mark {
    position: absolute;
    left: 90px; top: 110px;
    width: 160px;
    text-align: center;
    color: var(--ink);
    font-weight: 500;
    font-size: 72px;
    line-height: 1;
  }
  .divider {
    position: absolute;
    left: 263px; top: 85px;
    width: 2px; height: 160px;
    background: var(--rule);
  }
  .contact {
    position: absolute;
    left: 299px; top: 91px;
    color: var(--ink);
    font-size: 15.5px;
    line-height: 20px;
  }
  .contact__name {
    color: var(--brand-blue);
    font-weight: 500;
    font-size: 20.5px;
    line-height: 26px;
  }
  .contact__title { margin-bottom: 15px; }
  .contact__address { margin-bottom: 5px; }
  .contact__line { display: flex; align-items: center; gap: 6px; }
  .contact__line svg { flex: none; }

  .footer-band { position: absolute; left: 0; bottom: 0; width: 598px; height: 60px; }
  .services {
    position: absolute;
    left: 0; right: 0; bottom: 10px;
    text-align: center;
    color: var(--white);
    font-size: 15.5px;
  }
</style>
</head>
<body>
  <section class="card card--front" aria-label="Card front">
    <div class="front-mark">RK</div>
    <p class="front-company">R. K. Belvard &amp; Associates, Inc</p>
  </section>

  <section class="card card--back" aria-label="Card back">
    <div class="back-mark">RK</div>
    <div class="divider"></div>
    <div class="contact">
      <p class="contact__name">Gregor Belvard</p>
      <p class="contact__title">Accountant</p>
      <p>4219 NW 168th ST</p>
      <p class="contact__address">Cedarbrook, Florida 33081</p>
      <p class="contact__line">
        <svg width="14" height="14" viewBox="0 0 24 24" aria-hidden="true"><path fill="#0a6db4" d="M6.6 10.8a15.1 15.1 0 0 0 6.6 6.6l2.2-2.2c.3-.3.7-.4 1-.2 1.1.4 2.3.6 3.6.6.6 0 1 .4 1 1V20c0 .6-.4 1-1 1A17 17 0 0 1 3 4c0-.6.4-1 1-1h3.5c.6 0 1 .4 1 1 0 1.3.2 2.5.6 3.6.1.3 0 .7-.2 1z"/></svg>
        (305) 555-0187
      </p>
      <p class="contact__line">
        <svg width="14" height="11" viewBox="0 0 14 11" aria-hidden="true"><rect x="0.75" y="0.75" width="12.5" height="9.5" fill="none" stroke="#0a6db4" stroke-width="1.5"/><path d="M1 1l6 5 6-5" fill="none" stroke="#0a6db4" stroke-width="1.5"/></svg>
        greg.belvard@quillmarsh.com
      </p>
    </div>
    <svg class="footer-band" viewBox="0 0 598 60" preserveAspectRatio="none" aria-hidden="true">
      <path d="M0 10 Q299 30 598 10 L598 60 L0 60 Z" fill="#0a6db4"/>
      <path d="M0 4 Q299 24 598 4" fill="none" stroke="#222222" stroke-width="2"/>
    </svg>
    <p class="services">Accounting | Tax Preparation Services | Bookkeeping</p>
  </section>
</body>
</html>
```